Bamboo Wash Cloth Package Design

We need packaging designed for Bamboo Washcloths the Package will be: 25 cm x 14 cm x 4 cm
I am attaching Pictures of the box and our logo. All the language that is on the box will need to be on there, but can be moved and customized.
In addition to our logo the front of the box should have on it:
7 100% Natural Bamboo Washcloths
1 for Every Day of the Week
Ultra Soft
7 Pack of 10" by 10" Washcloths
Free from Chemicals, Toxins and Dyes
Perfect for Sensitive and Delicate Skin
Generously Sized
All Natural Bamboo
The Back should have our logo and the following language:
The Willow Nest Collection's premium 100% natural bamboo washcloths are the softest most gentle washcloths available. They are perfect for babies' delicate skin and for adults.
Willow Nest only uses the highest quality bamboo on the planet. Our perfectly sized washcloths are carefully woven into plush goodness featuring maximum absorbency and durability.
These eco-friendly washcloths, created from a sustainable source, are naturally antibacterial, hypoallergenic, and free from all dyes, chemicals, and toxins. They are comfort guaranteed and will leave you and your baby's skin feeling as pristine as nature intended.
The icons on the bottom of the box should also be used.
Additional thoughts:
1. Would like to see Bamboo and a Baby Panda worked into the design.
2.The Box can be 4 color.
3. I am attaching 3 box Pictures. The first 2 are picture of what our box is like for reference.
4. the 3rd is an idea of the color scheme I'd like to see utilized.
Please let me know if you have any questions.
Target Market(s)
Mothers and people who are environmentally conscious
Look and feel

```html
<!DOCTYPE html>
<html lang="en">
<head>
<meta charset="utf-8">
<title>Willow Nest Bamboo Washcloth Box</title>
<link href="https://fonts.googleapis.com/css2?family=Nunito:wght@400;700;800&family=Yellowtail&family=Dosis:wght@400;500&display=swap" rel="stylesheet">
<style>
  :root{
    --leaf:#9aae5a;
    --leaf-light:#b9c97a;
    --leaf-dark:#4f6b2a;
    --ribbon:#55702e;
    --flap:#8fa64f;
    --red:#e8403e;
    --blue:#1670b8;
    --ink:#2f4a1c;
    --paper:#ffffff;
    --line:#8a8a8a;
  }
  *{box-sizing:border-box;margin:0;padding:0}
  html,body{width:1162px;height:1200px;overflow:hidden;background:var(--paper)}
  .dieline{position:relative;width:1162px;height:1200px;font-family:'Nunito',sans-serif}
  .panel{position:absolute;border:1px solid var(--line)}

  /* back panel (printed upside-down) */
  .back{left:184px;top:39px;width:790px;height:443px;transform:rotate(180deg);overflow:hidden;
    background:linear-gradient(to bottom,var(--paper) 0,var(--paper) 24%,var(--leaf) 40%,var(--leaf) 100%)}
  .back-scene{position:absolute;inset:0}
  .brand{position:absolute;left:0;right:0;display:flex;flex-direction:column;align-items:center;gap:4px}
  .brand-dot{border-radius:50%;background:var(--leaf-dark)}
  .brand-name{font-family:'Nunito',sans-serif;font-weight:800;color:var(--leaf-dark)}
  .back .brand{top:22px}
  .back .brand-dot{width:48px;height:48px}
  .back .brand-name{font-size:18px}
  .story{position:absolute;left:83px;top:134px;width:615px;height:202px;background:var(--paper);
    border:6px solid var(--red);outline:3px solid var(--blue);outline-offset:-11px;padding:14px 22px;
    font-size:12.2px;line-height:1.32;color:var(--ink);text-align:center;display:flex;flex-direction:column;justify-content:center;gap:8px}
  .care{position:absolute;top:342px;left:0;right:0;text-align:center;font-size:11.5px;line-height:1.35;color:#333}
  .care-icons{position:absolute;top:394px;left:309px;display:flex;gap:20px}
  .care-icons svg{width:30px;height:28px}

  /* top flap with banner */
  .lid{left:184px;top:482px;width:790px;height:125px;background:var(--paper)}
  .ribbon{position:absolute;overflow:visible}
  .ribbon-text{font-family:'Yellowtail',cursive;fill:var(--paper)}

  /* front */
  .front{left:184px;top:607px;width:790px;height:442px;overflow:hidden;background:var(--paper)}
  .front-scene{position:absolute;inset:0}
  .front .brand{top:16px}
  .front .brand-dot{width:58px;height:58px}
  .front .brand-name{font-size:17px}
  .window{position:absolute;left:134px;top:124px;width:521px;height:187px;border:1.5px solid rgba(255,255,255,.9);border-radius:9px}
  .badge-round{position:absolute;width:80px;height:80px;border-radius:50%;background:var(--red);border:3px solid #f47b6d;color:var(--paper);display:flex;align-items:center;justify-content:center;text-align:center}
  .badge-soft{left:28px;top:164px}
  .badge-soft span{font-family:'Yellowtail',cursive;font-size:19px;white-space:nowrap;transform:rotate(-14deg)}
  .badge-pack{left:680px;top:164px;gap:2px}
  .badge-pack .num{font-family:'Dosis',sans-serif;font-size:46px;line-height:1;font-weight:500}
  .badge-pack .col{display:flex;flex-direction:column;align-items:flex-start;text-align:left}
  .badge-pack .word{font-size:15px;line-height:1}
  .badge-pack .size{font-size:6.5px;font-weight:700;line-height:1.2;margin-top:3px;white-space:nowrap}
  .badge-week{position:absolute;left:13px;top:266px;width:105px;height:84px;background:var(--blue);border:2px solid #4e97d3;color:var(--paper);display:flex;align-items:center;gap:6px;padding:6px 8px}
  .badge-week .num{font-family:'Dosis',sans-serif;font-size:58px;line-height:1;font-weight:500}
  .badge-week .txt{font-size:12.5px;font-weight:800;line-height:1.05}
  .claims{position:absolute;left:67px;top:390px;width:648px;height:26px;background:var(--paper);border:2px dotted var(--red);outline:1px dotted var(--blue);
    font-family:'Dosis',sans-serif;font-size:13px;color:var(--leaf-dark);display:flex;align-items:center;justify-content:center;white-space:nowrap}

  /* side flaps */
  .side{position:absolute;top:607px;width:127px;height:442px;border:1px solid var(--line);background:var(--leaf)}
  .side-left{left:57px}
  .side-right{left:974px}
  .glue{position:absolute;top:612px;width:37px;height:432px;background:var(--flap);border:1px solid var(--line)}
  .glue-left{left:20px;border-radius:6px 0 0 6px}
  .glue-right{left:1101px;border-radius:0 6px 6px 0}
  .tuck{position:absolute;top:1049px}

  /* bottom */
  .base{left:184px;top:1049px;width:790px;height:128px;background:var(--paper)}
</style>
</head>
<body>
<main class="dieline">

  <!-- back panel -->
  <section class="panel back">
    <div class="back-scene" role="img" aria-label="Bamboo stalks, leaves, red and blue flowers and two baby pandas peeking from the corners"></div>
    <div class="brand">
      <span class="brand-dot"></span>
      <span class="brand-name">willow nest</span>
    </div>
    <div class="story">
      <p>The Willow Nest Collection's premium 100% natural bamboo washcloths are the softest most gentle washcloths available. They are perfect for babies' delicate skin and for adults.</p>
      <p>Willow Nest only uses the highest quality bamboo on the planet. Our perfectly sized washcloths are carefully woven into plush goodness featuring maximum absorbency and durability.</p>
      <p>These eco-friendly washcloths, created from a sustainable source, are naturally antibacterial, hypoallergenic, and free from all dyes, chemicals, and toxins. They are comfort guaranteed and will leave you and your baby's skin feeling as pristine as nature intended.</p>
    </div>
    <div class="care">
      Care Instruction :<br>
      Wash before use. Machine wash cold with like colors. Do not use bleach<br>
      Tumble dry low. No not iron. Made in China
    </div>
    <div class="care-icons">
      <svg viewBox="0 0 30 28" aria-label="Wash at 30"><path d="M2 6 L5 24 H25 L28 6" fill="none" stroke="#333" stroke-width="1.5"/><path d="M2 6 Q8 10 15 6 T28 6" fill="none" stroke="#333" stroke-width="1.5"/><text x="15" y="20" font-size="9" text-anchor="middle" fill="#333" font-family="Nunito,sans-serif">30</text></svg>
      <svg viewBox="0 0 30 28" aria-label="Do not bleach"><path d="M15 3 L28 25 H2 Z" fill="none" stroke="#333" stroke-width="1.5"/><path d="M4 3 L26 27 M26 3 L4 27" stroke="#333" stroke-width="1.5"/></svg>
      <svg viewBox="0 0 30 28" aria-label="Do not tumble dry hot"><rect x="3" y="2" width="24" height="24" fill="none" stroke="#333" stroke-width="1.5"/><circle cx="15" cy="14" r="8" fill="none" stroke="#333" stroke-width="1.5"/><path d="M3 2 L27 26 M27 2 L3 26" stroke="#333" stroke-width="1.5"/></svg>
      <svg viewBox="0 0 30 28" aria-label="Do not iron"><path d="M3 22 H27 L24 10 H10 Q4 12 3 22 Z" fill="none" stroke="#333" stroke-width="1.5"/><path d="M4 4 L26 26 M26 4 L4 26" stroke="#333" stroke-width="1.5"/></svg>
    </div>
  </section>

  <!-- top flap -->
  <section class="panel lid">
    <svg class="ribbon" style="left:67px;top:25px" width="650" height="78" viewBox="0 0 650 78">
      <path d="M0 32 L60 18 L48 40 L70 62 L10 72 Z" fill="var(--ribbon)"/>
      <path d="M590 2 L650 12 L628 32 L640 60 L575 48 Z" fill="var(--ribbon)"/>
      <path d="M60 10 Q330 -6 600 34 L596 70 Q330 30 62 54 Z" fill="var(--ribbon)"/>
      <path id="lid-arc" d="M70 42 Q330 14 596 62" fill="none"/>
      <text class="ribbon-text" font-size="29"><textPath href="#lid-arc" startOffset="50%" text-anchor="middle">100% Natural Bamboo Washcloths</textPath></text>
    </svg>
  </section>

  <!-- side flaps -->
  <div class="glue glue-left"></div>
  <div class="side side-left" role="img" aria-label="Bamboo stalks and leaves with red and blue flowers"></div>
  <div class="side side-right" role="img" aria-label="Bamboo stalks and leaves with red and blue flowers"></div>
  <div class="glue glue-right"></div>
  <svg class="tuck" style="left:57px" width="127" height="38" viewBox="0 0 127 38"><path d="M0 0 H127 L118 36 H6 Z" fill="var(--flap)" stroke="var(--line)"/></svg>
  <svg class="tuck" style="left:974px" width="127" height="38" viewBox="0 0 127 38"><path d="M0 0 H127 L121 36 H9 Z" fill="var(--flap)" stroke="var(--line)"/></svg>

  <!-- front panel -->
  <section class="panel front">
    <svg class="front-scene" width="790" height="442" viewBox="0 0 790 442" role="img" aria-label="Bamboo grove with baby pandas at the corners, leaves and red and blue flowers across a green meadow">
      <path d="M0 180 Q200 150 320 230 Q420 300 560 210 Q680 150 790 190 V442 H0 Z" fill="var(--leaf)"/>
      <path d="M0 0 H110 V200 Q50 190 0 200 Z" fill="var(--leaf-light)" opacity=".5"/>
      <path d="M680 0 H790 V200 Q740 190 680 200 Z" fill="var(--leaf-light)" opacity=".5"/>
    </svg>
    <div class="brand">
      <span class="brand-dot"></span>
      <span class="brand-name">willow nest</span>
    </div>
    <div class="window"></div>
    <div class="badge-round badge-soft"><span>Ultra Soft</span></div>
    <div class="badge-round badge-pack">
      <span class="num">7</span>
      <span class="col">
        <span class="word">pack</span>
        <span class="size">10" x 10"<br>Washcloths</span>
      </span>
    </div>
    <div class="badge-week">
      <span class="num">1</span>
      <span class="txt">for Every<br>Day of<br>the Week</span>
    </div>
    <svg class="ribbon" style="left:172px;top:330px" width="440" height="50" viewBox="0 0 440 50">
      <path d="M0 24 L40 14 L34 30 L46 44 L6 46 Z" fill="var(--ribbon)"/>
      <path d="M400 6 L440 10 L426 24 L434 42 L392 34 Z" fill="var(--ribbon)"/>
      <path d="M40 8 Q220 -2 404 22 L400 46 Q220 24 42 38 Z" fill="var(--ribbon)"/>
      <path id="front-arc" d="M46 30 Q220 12 400 40" fill="none"/>
      <text class="ribbon-text" font-size="20"><textPath href="#front-arc" startOffset="50%" text-anchor="middle">100% Natural Bamboo Washcloths</textPath></text>
    </svg>
    <div class="claims">Free from Chemicals, Toxins and Dyes | Perfect for Sensitive and Delicate Skin | Generously Sized | All Natural Bamboo</div>
  </section>

  <!-- bottom panel -->
  <section class="panel base"></section>

</main>
</body>
</html>
```